Lumo Grill-Wrap Stationery Design Project

We are a factory of the Doner kebab to distribute for restaurants and supermarkets.

what I need is

1- Presentation Folders cover for (Brochure , Letter and Business Card), the size ( 9"x12" Closed)

2- Envelopes, Size (DL , C5 and C4)

3- Letterhead (Standard).

Target Market(s)

Restaurants and supermarkets

Industry/Entity Type

Business

Requirements
Must have
• -Try to make the design related to the Business.

-Choose the same colors of the logo (Yellow, red and white).

-Try to make it seriously and high class business.

- The main logo with white background

```html
<!DOCTYPE html>
<html lang="en">
<head>
<meta charset="utf-8">
<title>Lumo Grill-Wrap Stationery</title>
<link href="https://fonts.googleapis.com/css2?family=Open+Sans:wght@400;600;700&display=swap" rel="stylesheet">
<style>
  :root{
    --brand-red:#c1272d;
    --brand-red-deep:#b1222a;
    --brand-gold:#d4a92a;
    --paper:#ffffff;
    --paper-mark:#efefef;
    --backdrop:#ececec;
    --ink:#555555;
    --rule:#c8c8c8;
  }
  html,body{margin:0;padding:0;overflow:hidden}
  body{width:1200px;height:1000px;background:var(--backdrop);position:relative;font-family:"Open Sans",Arial,sans-serif;color:var(--ink)}
  .sheet{position:absolute;box-sizing:border-box;overflow:hidden}

  .brand-name{font-family:"Open Sans",Arial,sans-serif;font-weight:400;text-transform:uppercase;letter-spacing:0.02em;white-space:nowrap;position:absolute;display:flex;align-items:center;gap:4px}
  .brand-name .dot{display:inline-block;border-radius:50%;background:var(--brand-gold);flex:none}
  .brand-on-red{color:var(--paper)}
  .brand-on-white{color:var(--brand-red)}

  .brand-watermark{position:absolute;font-family:"Open Sans",Arial,sans-serif;font-weight:700;text-transform:uppercase;line-height:0.95;white-space:nowrap}
  .watermark-dot{position:absolute;border-radius:50%}

  /* Presentation folder */
  .folder{left:83px;top:267px;width:340px;height:456px;background:var(--brand-red)}
  .folder .watermark-dot{left:40px;top:108px;width:34px;height:34px;background:var(--brand-red-deep)}
  .folder .brand-watermark{left:36px;top:156px;font-size:66px;color:var(--brand-red-deep)}
  .folder .brand-name{right:12px;bottom:14px;font-size:10px}
  .folder .dot{width:9px;height:9px}

  /* Letterhead */
  .letterhead{left:452px;top:283px;width:313px;height:441px;background:var(--paper)}
  .letterhead .brand-name{left:26px;top:43px;font-size:10px}
  .letterhead .dot{width:9px;height:9px}
  .letterhead .watermark-dot{left:128px;top:206px;width:20px;height:20px;background:var(--paper-mark)}
  .letterhead .brand-watermark{left:124px;top:234px;font-size:38px;color:var(--paper-mark)}
  .letterhead-footer{position:absolute;left:52px;right:26px;bottom:12px;border-top:0.6px solid var(--rule);padding-top:2px;font-size:3.6px;line-height:6px;text-align:center}

  /* Business cards */
  .card-front{left:808px;top:255px;width:126px;height:83px;background:var(--brand-red)}
  .card-front .brand-watermark{left:58px;top:2px;font-size:20px;color:var(--brand-red-deep)}
  .card-front .brand-name{left:50%;top:50%;transform:translate(-50%,-50%);font-size:7.5px}
  .card-front .dot{width:7px;height:7px}
  .card-back{left:986px;top:256px;width:127px;height:82px;background:var(--paper)}
  .card-back .brand-name{left:6px;top:13px;font-size:5px}
  .card-back .dot{width:5px;height:5px}
  .card-person{position:absolute;right:7px;top:38px;text-align:right}
  .card-person .person-name{font-size:6px;font-weight:700;color:var(--brand-red)}
  .card-person .person-role{font-size:4.5px;font-weight:700;color:var(--brand-gold)}
  .card-contact{position:absolute;left:7px;top:60px;font-size:3.2px;line-height:4.6px}

  /* DL envelope front */
  .envelope-front{left:798px;top:363px;width:328px;height:164px;background:var(--paper)}
  .envelope-front .brand-name{left:14px;top:34px;font-size:10px}
  .envelope-front .dot{width:9px;height:9px}
  .envelope-front .rule{position:absolute;left:14px;top:51px;width:84px;border-top:0.6px solid var(--rule)}
  .envelope-contact{position:absolute;left:14px;top:55px;font-size:3.6px;line-height:5px}

  /* Envelope back */
  .envelope-back{left:800px;top:553px;width:327px;height:165px;background:var(--paper)}
  .envelope-back svg{position:absolute;left:0;top:0}
  .envelope-back .brand-name{left:50%;top:30px;transform:translateX(-50%);font-size:7.5px}
  .envelope-back .dot{width:7px;height:7px}
</style>
</head>
<body>

<section class="sheet folder" aria-label="Presentation folder cover">
  <div class="watermark-dot"></div>
  <div class="brand-watermark" aria-hidden="true">Lumo<br>Grill-<br>Wrap</div>
  <div class="brand-name brand-on-red"><span class="dot"></span>Lumo Grill-Wrap</div>
</section>

<section class="sheet letterhead" aria-label="Letterhead">
  <div class="brand-name brand-on-white"><span class="dot"></span>Lumo Grill-Wrap</div>
  <div class="watermark-dot"></div>
  <div class="brand-watermark" aria-hidden="true">Lumo<br>Grill-<br>Wrap</div>
  <div class="letterhead-footer">
    Address: 48 Mill Lane, Eastfield, Postal Code, Country | Phone 555-0142 | Mobile 555-0187 | Fax 555-0143<br>
    E-Mail: daniel.hart@lumogrillwrap.com | Web: www.lumogrillwrap.com
  </div>
</section>

<section class="sheet card-front" aria-label="Business card front">
  <div class="brand-watermark" aria-hidden="true">Lumo<br>Grill-<br>Wrap</div>
  <div class="brand-name brand-on-red"><span class="dot"></span>Lumo Grill-Wrap</div>
</section>

<section class="sheet card-back" aria-label="Business card back">
  <div class="brand-name brand-on-white"><span class="dot"></span>Lumo Grill-Wrap</div>
  <div class="card-person">
    <div class="person-name">Daniel Hart</div>
    <div class="person-role">Manager</div>
  </div>
  <div class="card-contact">
    Address: 48 Mill Lane, Eastfield, Country<br>
    Phone 555-0142 | Fax 555-0143<br>
    E-Mail: daniel.hart@lumogrillwrap.com<br>
    Web: www.lumogrillwrap.com
  </div>
</section>

<section class="sheet envelope-front" aria-label="DL envelope front">
  <div class="brand-name brand-on-white"><span class="dot"></span>Lumo Grill-Wrap</div>
  <div class="rule"></div>
  <div class="envelope-contact">
    Address: 48 Mill Lane, Eastfield, Postal Code, Country<br>
    Phone 555-0142 | Fax 555-0143<br>
    E-Mail: daniel.hart@lumogrillwrap.com<br>
    Web: www.lumogrillwrap.com
  </div>
</section>

<section class="sheet envelope-back" aria-label="Envelope back with flap">
  <svg width="327" height="165" viewBox="0 0 327 165" aria-hidden="true">
    <polygon points="0,0 327,0 318,62 9,62" fill="var(--brand-red)"/>
    <line x1="0" y1="165" x2="120" y2="62" stroke="#e4e4e4" stroke-width="0.8"/>
    <line x1="327" y1="165" x2="207" y2="62" stroke="#e4e4e4" stroke-width="0.8"/>
  </svg>
  <div class="brand-name brand-on-red"><span class="dot"></span>Lumo Grill-Wrap</div>
</section>

</body>
</html>
```